SunHaven Webpage for Integrative and Holistic Psychiatric Practice

We need a webpage designed for a medical practice that focuses on integrative and holistic psychiatry. We focus on providing care to mothers and families. The name of the company is Sun Haven, incorporated, A Professional Medical Corporation.

We'd like the color palette to be earthy/natural with the same look and feel as our logo that's attached. We're not set on anything, so feel free to have fun with the palette. We just want it to be warm and inviting in particular for Moms!

We'd like to have our logo in the top left with links below it either centered or to the right. We really like websites like http://www.brightvalecare.example/home.html and http://www.marlowridgeclinic.example/site/ to give you an idea of what we're looking for.

For links, we're looking for the following. Dummy text is fine, we're still getting content together:

* Home
* About Us - this page would have headings for Directions, Staff, Appointment Scheduling
* Services Provided - headings for 8 different services
* Patient Resources - headings for Patient Forms, Fees, Articles
* FAQ
* Contact Us

The webpage will be hosted as an Office 365 Public Website, so feel free to use whatever SharePoint integration you would like, but it's not necessary.

Thank you!

```html
<!DOCTYPE html>
<html lang="en">
<head>
<meta charset="utf-8">
<title>SunHaven – Integrative &amp; Holistic Psychiatry</title>
<link href="https://fonts.googleapis.com/css2?family=Open+Sans:wght@400;600;700&display=swap" rel="stylesheet">
<style>
:root{
  --green:#6a9a2a;
  --green-dark:#4f7a1c;
  --orange:#f08a00;
  --brown-dark:#2a1a0d;
  --brown-bar:#a3580f;
  --text:#4a4a4a;
  --muted:#8a8a8a;
  --line:#d8d8d8;
  --band:#f4f3f1;
  --white:#ffffff;
}
*{margin:0;padding:0;box-sizing:border-box}
html,body{width:1200px;height:4032px;overflow:hidden}
body{position:relative;background:var(--white);font-family:"Open Sans",Arial,sans-serif;color:var(--text)}
.abs{position:absolute}

/* header */
.brand{left:62px;top:40px;display:flex;align-items:center;gap:16px}
.brand-mark{width:60px;height:60px;border-radius:50%;background:var(--green)}
.brand-name{font-size:36px;font-weight:600;color:var(--green-dark)}
.call{right:58px;top:62px;font-size:19px;color:var(--text)}
.call b{color:var(--orange);font-weight:600}
.chat{right:58px;top:116px;font-size:19px;display:flex;align-items:center;gap:12px}
.chat-dot{width:40px;height:40px;border-radius:50%;border:2px solid var(--line);background:#eee}
.nav{left:62px;top:196px;display:flex;gap:0;font-size:18px}
.nav a{color:var(--text);text-decoration:none;padding:0 22px 10px}
.nav a.active{color:var(--green);border-bottom:4px solid var(--green);padding-left:8px}
.nav span{color:var(--muted)}
.nav-rule{left:62px;right:62px;top:233px;height:1px;background:var(--line)}

/* hero */
.hero{left:0;top:274px;width:1200px;height:522px;background:linear-gradient(160deg,#e8efd8 0%,#c9d9a8 35%,#e9c9a8 65%,#7ca3c9 100%)}
.finder{left:0;top:796px;width:1200px;height:137px;background:var(--brown-dark)}
.finder p{position:absolute;left:62px;top:36px;font-size:22px;line-height:32px;color:var(--white)}
.finder p em{font-style:normal;color:var(--orange);font-size:26px}
.finder-btn{position:absolute;left:727px;top:34px;width:268px;height:66px;background:var(--orange);color:var(--brown-dark);font-size:22px;font-weight:600;display:flex;align-items:center;justify-content:center}

/* expertise */
.section-title{font-size:32px;font-weight:400;color:#666}
.expertise-title{left:0;width:1200px;top:985px;text-align:center}
.expertise-list{list-style:none;font-size:17px;color:#555}
.expertise-list li{height:41px;display:flex;align-items:center;gap:14px}
.expertise-list li::before{content:"";width:16px;height:16px;border-radius:50%;background:var(--green);flex:none;
  background-image:linear-gradient(var(--green),var(--green));box-shadow:inset 0 0 0 3px var(--green)}
.col-left{left:62px;top:1078px}
.col-right{left:627px;top:1078px}
.divider{left:267px;top:1560px;width:666px;height:1px;background:var(--line)}

/* about + articles */
.about-title{left:62px;top:1622px}
.articles-title{left:573px;top:1622px}
.video{left:62px;top:1725px;width:442px;height:312px;background:linear-gradient(135deg,#2a1a1a,#7a3a2e 55%,#d9c8c0)}
.play{position:absolute;left:191px;top:126px}
.about-text{left:62px;top:2068px;width:442px;font-size:15px;line-height:27px;color:#555}
.about-text b{color:#333}
.article{left:576px;width:566px;height:160px}
.article .thumb{position:absolute;left:0;top:0;width:172px;height:146px}
.article h3{position:absolute;left:220px;top:0;font-size:17px;font-weight:600;color:#444}
.article p{position:absolute;left:220px;top:28px;width:346px;font-size:14.5px;line-height:26px;color:#666}
.article .more{position:absolute;right:0;top:150px;font-size:12px;color:#555}
.t1{background:linear-gradient(135deg,#d8b79a,#8a5a3c)}
.t2{background:linear-gradient(135deg,#9ab4cc,#c9a27e)}
.t3{background:linear-gradient(135deg,#6a6a6a,#c8b49e)}

/* testimonials */
.testimonials{left:0;top:2360px;width:1200px;height:521px;background:var(--band)}
.testimonials .section-title{position:absolute;left:0;width:1200px;top:52px;text-align:center}
.quote{position:absolute;left:62px;top:136px;width:1076px;text-align:center;font-size:15px;line-height:32px;color:#777}
.avatar{position:absolute;left:62px;top:288px;width:110px;height:110px;border-radius:50%;border:4px solid var(--white);background:linear-gradient(135deg,#f0d8c0,#c99a6a)}
.patient{position:absolute;left:192px;top:330px;font-size:19px;color:#444}
.dots{position:absolute;left:0;width:1200px;top:450px;display:flex;justify-content:center;gap:10px}
.dots i{width:11px;height:11px;border-radius:50%;background:#ccc}
.dots i.on{background:var(--green)}

/* contact */
.contact-title{left:0;width:1200px;top:2943px;text-align:center}
.map{left:62px;top:3039px;width:511px;height:425px;background:linear-gradient(135deg,#ecebe4,#e2dfd2 50%,#f2e8c4)}
.field{border:1px solid var(--line);font-size:14px;color:#888;padding:0 14px;display:flex;align-items:center;height:52px}
.field i{color:#d33;font-style:normal;margin-left:3px}
.f-name{left:627px;top:3046px;width:250px}
.f-phone{left:892px;top:3046px;width:250px}
.f-email{left:627px;top:3112px;width:515px}
.f-comment{left:627px;top:3178px;width:515px;height:196px;align-items:flex-start;padding-top:14px}
.submit{left:916px;top:3406px;width:226px;height:62px;border:1px solid var(--line);font-size:18px;color:#555;display:flex;align-items:center;justify-content:center}

/* footer */
.footer{left:0;top:3533px;width:1200px;height:405px;background:var(--brown-dark);color:#e9e2da}
.footer h4{position:absolute;top:70px;font-size:19px;font-weight:400;letter-spacing:.5px;color:var(--white)}
.f-col1{left:62px}.f-col2{left:453px}.f-col3{left:847px}
.f-text{position:absolute;font-size:14px;line-height:28px}
.social{position:absolute;left:453px;top:138px;display:flex;gap:10px}
.social i{width:60px;height:60px;border-radius:50%;background:var(--white)}
.social i:first-child,.social i:nth-child(2){background:var(--orange)}
.news-title{top:248px !important}
.news{position:absolute;left:453px;top:285px;width:292px;height:46px;background:var(--white);display:flex}
.news span{flex:1;font-size:14px;color:#999;padding-left:12px;display:flex;align-items:center}
.news b{width:92px;background:var(--brown-bar);color:var(--white);font-weight:400;font-size:16px;display:flex;align-items:center;justify-content:center;margin:4px}
.top-btn{position:absolute;left:1090px;top:244px;width:50px;height:50px;border-radius:50%;background:var(--white)}
.bottom-bar{left:0;top:3938px;width:1200px;height:94px;background:var(--brown-bar);color:var(--white);font-size:14px}
.bottom-bar p{position:absolute;left:62px;top:36px}
</style>
</head>
<body>

<header>
  <div class="abs brand"><span class="brand-mark"></span><span class="brand-name">SunHaven</span></div>
  <div class="abs call">Call Now : <b>000 -000- 0000</b></div>
  <div class="abs chat">Live Chat : <span class="chat-dot"></span></div>
  <nav class="abs nav">
    <a class="active" href="#">Home</a><span>/</span>
    <a href="#">About us</a><span>/</span>
    <a href="#">Services</a><span>/</span>
    <a href="#">Patient Resources</a><span>/</span>
    <a href="#">FAQ</a><span>/</span>
    <a href="#">Contact us</a>
  </nav>
  <div class="abs nav-rule"></div>
</header>

<div class="abs hero" role="img" aria-label="Photo of a smiling family of four outdoors"></div>

<section class="abs finder">
  <p>If you're here to find a <em>Psychiatrist or therapist</em> who<br>takes your health insurance,you've come to right place.</p>
  <div class="finder-btn">Find a office near you</div>
</section>

<h2 class="abs section-title expertise-title">Areas of expertise:</h2>
<ul class="abs expertise-list col-left">
  <li>Alzheimer's Disease</li>
  <li>Anxiety Disorders</li>
  <li>Autism with behavioral disturbances</li>
  <li>Attention Deficit Disorder</li>
  <li>Drug and Alcohol Abuse</li>
  <li>Bipolar Disorders</li>
  <li>Couples Problems</li>
  <li>Depression</li>
  <li>Complex Physical/ Psychosomatic Conditions</li>
</ul>
<ul class="abs expertise-list col-right">
  <li>Eating Disorders</li>
  <li>Court ordered or Insurance Review Evaluations</li>
  <li>Panic Disorder</li>
  <li>Behavioral Problems</li>
  <li>Pain Problems</li>
  <li>Psychosomatic Conditions</li>
  <li>Schizophrenia</li>
  <li>OCD</li>
</ul>
<div class="abs divider"></div>

<h2 class="abs section-title about-title">About us</h2>
<h2 class="abs section-title articles-title">Latest Article</h2>

<div class="abs video" role="img" aria-label="Video still of the practice's lead psychiatrist">
  <svg class="play" width="60" height="60" viewBox="0 0 60 60"><circle cx="30" cy="30" r="30" fill="#d62222"/><path d="M24 18 L42 30 L24 42 Z" fill="#fff"/></svg>
</div>
<p class="abs about-text"><b>Dr. Helena Marsh</b> and her staff welcome you to The Mind &amp; Body House. Our practice is devoted to helping women improve their appearance through facial cosmetic procedures.<br>Today, traditional face lifts of yesterday are largely a thing of the past. With today's new facial cosmetic techniques like Injectable Cosmetic, Fillers, and Laser Treatments, we can help women look</p>

<article class="abs article" style="top:1722px">
  <div class="thumb t1" role="img" aria-label="Photo of a mother and daughter talking"></div>
  <h3>Lorem Ipsum is simply dummy text of</h3>
  <p>and typesetting industry. Lorem Ipsum has been the industry's standard dummy text ever since the Lorem Ipsum has been ...</p>
  <span class="more">READ MORE</span>
</article>
<article class="abs article" style="top:1938px">
  <div class="thumb t2" role="img" aria-label="Photo of a child studying at a desk"></div>
  <h3>Lorem Ipsum is simply dummy text of</h3>
  <p>and typesetting industry. Lorem Ipsum has been the industry's standard dummy text ever since the Lorem Ipsum has been ...</p>
  <span class="more">READ MORE</span>
</article>
<article class="abs article" style="top:2147px">
  <div class="thumb t3" role="img" aria-label="Photo of a worried child"></div>
  <h3>Lorem Ipsum is simply dummy text of</h3>
  <p>and typesetting industry. Lorem Ipsum has been the industry's standard dummy text ever since the Lorem Ipsum has been ...</p>
  <span class="more">READ MORE</span>
</article>

<section class="abs testimonials">
  <h2 class="section-title">What Patients Are Saying</h2>
  <p class="quote">" Lorem Ipsum is simply dummy text of the printing and typesetting industry. Lorem Ipsum has been the industry's standard dummy text ever since the 1500s, when an unknown printer took a galley of type and scrambled it to make a type specimen book. It has survived not only five centuries, but also the leap into electronic typesetting, remaining essentially unchanged. "</p>
  <div class="avatar" role="img" aria-label="Portrait of the patient"></div>
  <span class="patient">Lena Hartley</span>
  <div class="dots"><i class="on"></i><i></i><i></i></div>
</section>

<h2 class="abs section-title contact-title">Contact us</h2>
<div class="abs map" role="img" aria-label="Street map showing the office location"></div>
<div class="abs field f-name">Name<i>*</i></div>
<div class="abs field f-phone">Phone no<i>*</i></div>
<div class="abs field f-email">Email Address<i>*</i></div>
<div class="abs field f-comment">Your Comment goes here......</div>
<div class="abs submit">Submit your Message</div>

<footer class="abs footer">
  <h4 class="f-col1">CONTACT US</h4>
  <p class="f-text" style="left:62px;top:138px">The Mind &amp; Body House<br>2210 Larkspur Rd, Suite 100<br>Fairhollow, Tx 70000<br>Phone No. (555) 014-3200</p>
  <h4 class="f-col2">STAY CONNECTED</h4>
  <div class="social" aria-label="Social links"><i></i><i></i><i></i><i></i></div>
  <h4 class="f-col2 news-title">NEWSLETTER SINGUP</h4>
  <div class="news"><span>Email Address</span><b>Sign up</b></div>
  <h4 class="f-col3">QUICK LINKS</h4>
  <p class="f-text" style="left:847px;top:118px;font-size:13px;line-height:28px">Home<br>About us<br>Services<br>FAQ<br>Blog<br>Contact us</p>
  <svg class="top-btn" viewBox="0 0 50 50"><circle cx="25" cy="25" r="25" fill="#fff"/><path d="M17 29 L25 21 L33 29" stroke="#2a1a0d" stroke-width="3" fill="none"/></svg>
</footer>
<div class="abs bottom-bar"><p>©2014 - SunHaven.example All Rights Reserved</p></div>

</body>
</html>
```